Professional law firm looking for new professional and eye-catching business card design

Law firm in need of new business card design using existing firm logo and firm colors on thick card stock. Firm colors are navy blue, cyan blue, and gray. Please use firm's logo either on the back of the card or on the front and back. I am looking for something eye-catching and resonating but also professional.

Target Market(s)

Law firm growth by attracting clients with professional, creative, and attractive business cards.

Industry/Entity Type

Legal/Law Firm

Contact Information for Business Card

Name: Derek T. Halloway, Esq., Address: 517 E. Quintley Blvd., P.O. Box 641, Larkmoor, OR 97390, Phone numbers: (555) 555-0187 Office, (555) 555-0142 Fax, email address: DerekH@hqlegalfx.com, website: www.HQLegalFX.com

Font styles to use
Other font styles liked:
• Font as close as possible to matching law firm logo.

Requirements
Must have
• Must have business card details and law firm logo with law firm colors.

```html
<!DOCTYPE html>
<html lang="en">
<head>
<meta charset="utf-8">
<title>HQ Legal — Business Card</title>
<link rel="stylesheet" href="https://fonts.googleapis.com/css2?family=Questrial&family=Poppins:ital,wght@0,200;0,300;1,300&display=swap">
<style>
  :root {
    --page-bg: #e6e7e9;
    --card-bg: #000000;
    --cyan: #0aa5e6;
    --gray-text: #c9c9c9;
    --light-text: #e8e8e8;
  }
  * { margin: 0; padding: 0; box-sizing: border-box; }
  html, body {
    width: 1200px; height: 1200px; overflow: hidden;
    background: var(--page-bg);
  }
  .stage { position: relative; width: 1200px; height: 1200px; }
  .card {
    position: absolute; left: 247px; width: 697px; height: 418px;
    background: var(--card-bg);
    font-family: "Poppins", sans-serif;
    color: var(--gray-text);
    text-align: center;
  }
  .card--front { top: 140px; }
  .card--back { top: 656px; }

  .firm-mark {
    position: absolute; left: 0; right: 0;
    display: flex; align-items: center; justify-content: center;
    font-family: "Questrial", sans-serif; color: var(--cyan);
    letter-spacing: 0.08em; line-height: 1;
  }
  .firm-mark__square { background: var(--cyan); display: block; }
  .card--front .firm-mark { top: 62px; gap: 12px; font-size: 30px; }
  .card--front .firm-mark__square { width: 22px; height: 22px; }
  .card--back .firm-mark { top: 152px; gap: 20px; font-size: 52px; }
  .card--back .firm-mark__square { width: 38px; height: 38px; }

  .attorney-name {
    position: absolute; left: 0; right: 0; top: 152px;
    font-family: "Questrial", sans-serif; font-weight: 400;
    font-size: 34px; color: var(--cyan);
  }
  .attorney-title {
    position: absolute; left: 0; right: 0; top: 198px;
    font-style: italic; font-weight: 300; font-size: 19px; color: var(--gray-text);
  }
  .rule {
    position: absolute; top: 236px; left: 206px; width: 284px; height: 1.5px;
    background: var(--cyan);
  }
  .contact-row {
    position: absolute; left: 0; right: 0; top: 250px;
    font-weight: 300; font-size: 16.5px;
    display: flex; justify-content: center; gap: 22px;
  }
  .contact-row .label { color: var(--cyan); font-family: "Questrial", sans-serif; margin-right: 8px; }
  .address {
    position: absolute; left: 0; right: 0; top: 288px;
    font-weight: 300; font-size: 16px; line-height: 25px;
  }
  .web-row {
    position: absolute; left: 0; right: 0; top: 356px;
    font-weight: 300; font-size: 14.5px;
    display: flex; justify-content: center; align-items: center; gap: 20px;
  }
  .web-row .divider { width: 1.5px; height: 18px; background: var(--cyan); }

  .back-line {
    position: absolute; top: 367px; height: 1.5px; width: 201px; background: var(--cyan);
  }
  .back-line--left { left: 0; }
  .back-line--right { right: 0; }
  .back-website {
    position: absolute; left: 0; right: 0; top: 352px;
    font-weight: 300; font-size: 21px; color: var(--light-text);
  }
</style>
</head>
<body>
<main class="stage">
  <section class="card card--front">
    <div class="firm-mark"><span class="firm-mark__square"></span><span>HQ LEGAL</span></div>
    <h1 class="attorney-name">Derek T. Halloway, Esq.</h1>
    <p class="attorney-title">Attorney at Law</p>
    <div class="rule"></div>
    <p class="contact-row">
      <span><span class="label">PHONE</span>(555) 555-0187</span>
      <span><span class="label">FAX</span>(555) 555-0142</span>
    </p>
    <p class="address">517 E. Quintley Blvd.<br>P.O. Box 641, Larkmoor, OR 97390</p>
    <p class="web-row">
      <span>DerekH@hqlegalfx.com</span>
      <span class="divider"></span>
      <span>www.HQLegalFX.com</span>
    </p>
  </section>

  <section class="card card--back">
    <div class="firm-mark"><span class="firm-mark__square"></span><span>HQ LEGAL</span></div>
    <div class="back-line back-line--left"></div>
    <p class="back-website">www.HQLegalFX.com</p>
    <div class="back-line back-line--right"></div>
  </section>
</main>
</body>
</html>
```